Single-sided business card for restaurant bellwether with new logo made on this site

Business card options with new logo including restaurant name, address, phone number and website. This business card is single-sided only and will be presented at the hostess desk for clients to take. I would like to see options based on a cream card background, a white card background, a yellow card background and a burgundy colored background. It needs to be elegant and traditional.

Target Market(s)

local and international crowd

Industry/Entity Type

restaurant

Contact Information for Business Card

address, website and phone number

Font styles to use
Serif

Colors
EE7325
F08F49
F5BC92
FAE3D3
FDF4ED

Requirements
Must have
• new logo, address, phone number, website
Should not have
• more than three colors

```html
<!DOCTYPE html>
<html lang="es">
<head>
<meta charset="UTF-8">
<title>Bellwether – Tarjetas de presentación</title>
<link href="https://fonts.googleapis.com/css2?family=Poppins:wght@600&display=swap" rel="stylesheet">
<style>
  :root {
    --backdrop: #dcdcdc;
    --paper-white: #f3f1ed;
    --gold: #e7b52c;
    --gold-deep: #e2ab27;
    --burgundy: #45191b;
  }
  * { box-sizing: border-box; margin: 0; padding: 0; }
  html, body {
    width: 1200px; height: 960px; overflow: hidden;
    background: var(--backdrop);
    font-family: "Poppins", sans-serif;
  }
  .card {
    position: absolute; top: 116px;
    width: 401px; height: 701px;
    color: var(--burgundy);
    text-align: center;
  }
  .card--white { left: 158px; background: var(--paper-white); --accent: var(--gold); --mark: var(--gold); }
  .card--gold { left: 630px; background: var(--gold); --accent: var(--burgundy); --mark: var(--burgundy); }
  .card__frame {
    position: absolute; inset: 9px 9px 9px 9px;
    border: 5px solid var(--accent);
  }
  .brand__mark {
    position: absolute; left: 128px; top: 59px;
    width: 150px; height: 150px;
    background: var(--mark);
  }
  .brand__name {
    position: absolute; left: 0; right: 0; top: 228px;
    font-weight: 600; font-size: 34px; letter-spacing: 3px;
    line-height: 1;
  }
  .contact {
    position: absolute; left: 0; right: 0; top: 459px;
    font-weight: 600;
  }
  .contact__address { font-size: 17.5px; line-height: 23.5px; }
  .contact__lines { margin-top: 10px; font-size: 16px; line-height: 23px; letter-spacing: 0.6px; }
</style>
</head>
<body>
  <section class="card card--white">
    <div class="card__frame"></div>
    <div class="brand__mark" aria-hidden="true"></div>
    <h1 class="brand__name">BELLWETHER</h1>
    <div class="contact">
      <p class="contact__address">Jacaranda 418<br>Bahías del Sol<br>Oaxaca, Mexico CP 70990</p>
      <p class="contact__lines">Reservaciones • 958-555-0142<br>www.bellwether.com.mx</p>
    </div>
  </section>

  <section class="card card--gold">
    <div class="card__frame"></div>
    <div class="brand__mark" aria-hidden="true"></div>
    <h1 class="brand__name">BELLWETHER</h1>
    <div class="contact">
      <p class="contact__address">Jacaranda 418<br>Bahías del Sol<br>Oaxaca, Mexico CP 70990</p>
      <p class="contact__lines">Reservaciones • 958-555-0142<br>www.bellwether.com.mx</p>
    </div>
  </section>
</body>
</html>
```